Exhibition Stand Design for innovative Social Business

We are an innovative social business empowering people to value nature through ZUN, a complementary digital currency. We have attached the TEK_ZUN branding document, and are needing a design for our exhibition stand (https://fairbuildlab.com/produit/stand-parapluie-classic-pvc-3x4c/. The attached doc mocks up a stand on page 32, though we would like some messaging included, in line with our website www.tekzun.ch. You will see there how the branding concept has been implemented with the TEK:GROW, SHARE, THRIVE wording, as well as Everyone wins. Our green colours are included in the branding document. Many thanks!

Industry/Entity Type

Environment

Font styles to use
Other font styles liked:
• As per our attached fonts

Requirements
Must have
• Our attached branding guidelines gives our look and feel - Innovative / Dynamic / Vibrant / Reliable / Accessible / Connected.

```html
<!DOCTYPE html>
<html lang="en">
<head>
<meta charset="utf-8">
<title>TekZun exhibition stand backdrop</title>
<link href="https://fonts.googleapis.com/css2?family=Montserrat:wght@600;700&display=swap" rel="stylesheet">
<style>
  :root {
    --page: #f2f3f2;
    --teal: #71c8b4;
    --mint: #7cc993;
    --green: #63bb47;
    --ink: #111111;
    --white: #ffffff;
  }
  html, body {
    margin: 0;
    padding: 0;
    width: 766px;
    height: 1200px;
    overflow: hidden;
    background: var(--page);
  }
  .canvas {
    position: relative;
    width: 766px;
    height: 1200px;
    display: flex;
    align-items: center;
  }
  .backdrop {
    position: relative;
    width: 766px;
    height: 576px;
    overflow: hidden;
    background: linear-gradient(100deg, var(--teal) 0%, var(--mint) 45%, var(--green) 100%);
    font-family: "Montserrat", sans-serif;
  }
  .backdrop__bubbles {
    position: absolute;
    inset: 0;
  }
  .brand {
    position: absolute;
    left: 58px;
    top: 230px;
  }
  .brand__name {
    margin: 0;
    font-weight: 700;
    font-size: 78px;
    line-height: 1;
    letter-spacing: -1px;
    color: var(--ink);
  }
  .brand__url {
    margin: 10px 0 0 2px;
    font-weight: 600;
    font-size: 26px;
    line-height: 1;
    color: var(--white);
  }
  .values {
    position: absolute;
    left: 456px;
    top: 222px;
    margin: 0;
    padding: 0;
    list-style: none;
    font-weight: 700;
    font-size: 35px;
    line-height: 35px;
    letter-spacing: -0.5px;
  }
  .values__item--light { color: var(--white); }
  .values__item--dark { color: var(--ink); }
</style>
</head>
<body>
<main class="canvas">
  <section class="backdrop">
    <svg class="backdrop__bubbles" width="766" height="576" viewBox="0 0 766 576" aria-hidden="true">
      <defs>
        <linearGradient id="bubble-top" x1="0" y1="0" x2="1" y2="0">
          <stop offset="0" stop-color="#ffffff" stop-opacity="0.95"/>
          <stop offset="1" stop-color="#ffffff" stop-opacity="0.35"/>
        </linearGradient>
        <linearGradient id="bubble-bottom" x1="0" y1="0" x2="1" y2="0">
          <stop offset="0" stop-color="#ffffff" stop-opacity="0.9"/>
          <stop offset="1" stop-color="#ffffff" stop-opacity="0.2"/>
        </linearGradient>
        <linearGradient id="bubble-small" x1="0" y1="0" x2="1" y2="1">
          <stop offset="0" stop-color="#ffffff" stop-opacity="0.75"/>
          <stop offset="1" stop-color="#ffffff" stop-opacity="0.25"/>
        </linearGradient>
      </defs>
      <circle cx="640" cy="62" r="150" fill="url(#bubble-top)"/>
      <circle cx="118" cy="516" r="150" fill="url(#bubble-bottom)"/>
      <circle cx="572" cy="423" r="73" fill="url(#bubble-small)"/>
    </svg>

    <div class="brand">
      <h1 class="brand__name">TekZun</h1>
      <p class="brand__url">www.tekzun.ch</p>
    </div>

    <ul class="values">
      <li class="values__item values__item--light">INNOVATIVE</li>
      <li class="values__item values__item--light">DYNAMIC</li>
      <li class="values__item values__item--light">VIBRANT</li>
      <li class="values__item values__item--dark">RELIABLE</li>
      <li class="values__item values__item--dark">ACCESSIBLE</li>
      <li class="values__item values__item--dark">CONNECTED</li>
    </ul>
  </section>
</main>
</body>
</html>
```